Postcard Design

I am an attorney in Pittsburgh. Here and across country, companies are sending data with names, address and new criminal charges for people. This has resulted in some people getting 12 or more of these letters. I want to do a postcard because one does not need to open a postcard. I also want to be delicate since there is no sealed envelope. I want to throw in other matters other than criminal so it does not look like the person is necessarily charged with a crime.
At top would be "Law Office of Dorian F. Haslbeck"
Then:
Need an Attorney?
Attorney Dorian F. Haslbeck has 25 Years of Experience
Free Consultation - Affordable Fees - Credit Cards Accepted
-All Criminal Matters
-Most Civil Matters
-DUI / Traffic Citations / License Restoration
412-555-0187
www.lakesidedefenselawyer.example
www.dfhcounsel.example

My CTQ ranking is A+ but I am not sure they give a logo with the rating. I have all my logos at www.lakesidedefenselawyer.example The purpose of the two websites is these are postcards. I want no one to think oh this person is charged with a crime.

Industry/Entity Type

Attorney

```html
<!DOCTYPE html>
<html lang="en">
<head>
<meta charset="utf-8">
<title>Law Office of Dorian F. Haslbeck – Postcard</title>
<link href="https://fonts.googleapis.com/css2?family=Fira+Sans+Condensed:wght@500;600&family=Fira+Sans:wght@300;400;500;600&display=swap" rel="stylesheet">
<style>
  :root {
    --red: #9b1218;
    --black: #0b0b0b;
    --ink: #1a1a1a;
    --white: #ffffff;
    --page: #e6e4e1;
    --rule: #b9b9b9;
  }
  * { box-sizing: border-box; margin: 0; padding: 0; }
  html, body { width: 1005px; height: 1200px; overflow: hidden; }
  body { background: var(--page); font-family: "Fira Sans", sans-serif; color: var(--ink); position: relative; }

  .card { position: absolute; left: 40px; width: 925px; height: 575px; background: var(--white); overflow: hidden; box-shadow: 0 2px 6px rgba(0,0,0,.18); }
  .card--front { top: 15px; }
  .card--back { top: 610px; }

  .heading { font-family: "Fira Sans Condensed", sans-serif; }
  .check { width: 15px; height: 15px; flex: none; }

  /* Front */
  .front__office { position: absolute; left: 24px; top: 30px; font-size: 22px; font-weight: 400; }
  .front__brand { position: absolute; left: 460px; top: 22px; display: flex; align-items: center; gap: 14px; }
  .badge { width: 70px; height: 70px; border-radius: 50%; background: #232a4a; border: 4px solid #b08a3e; }
  .front__brand-text { font-family: "Fira Sans Condensed", sans-serif; font-weight: 600; color: var(--red); font-size: 17px; line-height: 21px; }
  .front__photo { position: absolute; left: 270px; top: 100px; width: 655px; height: 405px;
    clip-path: polygon(145px 0, 100% 0, 100% 100%, 0 100%);
    background: linear-gradient(110deg, #d9dde2 0%, #f1f2f4 35%, #6b5a4c 62%, #2e2a28 100%); }
  .front__headline { position: absolute; left: 24px; top: 80px; line-height: 1; }
  .front__headline .l1 { display: block; font-size: 50px; font-weight: 600; color: var(--black); }
  .front__headline .l2 { display: block; font-size: 56px; font-weight: 600; color: var(--red); margin-top: 2px; }
  .front__lead { position: absolute; left: 24px; top: 232px; width: 340px; font-size: 19px; line-height: 24px; color: var(--red); font-weight: 500; }
  .front__matters { position: absolute; left: 24px; top: 287px; list-style: none; font-size: 15px; font-weight: 600; line-height: 23.5px; }
  .front__cta { position: absolute; left: 0; top: 352px; width: 430px; height: 75px; background: var(--black);
    clip-path: polygon(0 0, 100% 0, 94% 100%, 0 100%);
    color: var(--white); font-size: 13.5px; font-weight: 600; line-height: 22px; padding: 17px 0 0 27px; letter-spacing: .2px; }
  .front__perks { position: absolute; left: 20px; top: 440px; list-style: none; font-size: 16.5px; font-weight: 300; line-height: 23.5px; }
  .front__perks li, .back__questions li { display: flex; align-items: center; gap: 8px; }
  .front__bar { position: absolute; left: 0; top: 515px; width: 925px; height: 60px; background: var(--black); }
  .front__phone { position: absolute; left: 0; top: 0; width: 270px; height: 60px; background: var(--red);
    clip-path: polygon(0 0, 100% 0, 92% 100%, 0 100%);
    display: flex; align-items: center; gap: 14px; padding-left: 26px; color: var(--white); font-weight: 600; font-size: 21px; }
  .front__web { position: absolute; right: 30px; top: 0; height: 60px; display: flex; align-items: center; gap: 12px; color: var(--white); font-size: 19px; font-weight: 500; }

  /* Back */
  .back__title { position: absolute; left: 32px; top: 38px; font-size: 24px; line-height: 30px; font-weight: 600; color: var(--red); }
  .back__tag { position: absolute; left: 0; top: 113px; width: 468px; height: 50px; background: var(--red); color: var(--white);
    font-family: "Fira Sans Condensed", sans-serif; font-weight: 500; font-size: 22px; display: flex; align-items: center; padding-left: 30px; }
  .back__questions { position: absolute; left: 0; top: 167px; width: 468px; height: 185px; background: var(--black); list-style: none;
    color: var(--white); font-size: 19.5px; font-weight: 300; line-height: 32.5px; padding: 12px 0 0 30px; }
  .back__photo { position: absolute; left: 2px; top: 356px; width: 464px; height: 133px;
    background: linear-gradient(100deg, #3a3f48 0%, #6d7480 40%, #2d3a5a 70%, #c9ccd2 100%); }
  .back__cta { position: absolute; left: 0; top: 492px; width: 468px; height: 83px; background: var(--red); color: var(--white);
    font-size: 13.5px; font-weight: 600; line-height: 22px; text-align: center; padding-top: 19px; }
  .back__address { position: absolute; left: 505px; top: 30px; font-size: 11.5px; line-height: 16.5px; }
  .back__address .name { color: var(--red); }
  .back__stamp { position: absolute; left: 770px; top: 23px; width: 108px; height: 72px; border: 1px solid var(--rule); }
  .back__lines { position: absolute; left: 580px; top: 185px; width: 285px; }
  .back__lines span { display: block; height: 31px; border-bottom: 1px solid var(--rule); }
  .back__seals { position: absolute; left: 670px; top: 480px; display: flex; align-items: center; gap: 12px; }
  .seal--gold { width: 70px; height: 70px; border-radius: 50%; background: #1e3f7a; border: 4px solid #c7a247; }
  .back__rating { display: flex; align-items: center; gap: 4px; color: #1e5a8a; font-weight: 600; font-size: 13px; }
  .back__rating i { width: 10px; height: 10px; background: #1e5a8a; }
</style>
</head>
<body>

<svg width="0" height="0" style="position:absolute">
  <symbol id="tick" viewBox="0 0 16 16">
    <rect x="1.5" y="2.5" width="11" height="11" rx="2" fill="none" stroke="currentColor" stroke-width="1.6"/>
    <path d="M4.5 7.5l2.5 2.5 7-7.5" fill="none" stroke="currentColor" stroke-width="1.8" stroke-linecap="round"/>
  </symbol>
</svg>

<section class="card card--front">
  <div class="front__photo" role="img" aria-label="Photo of an attorney writing at a desk beside a laptop and a bronze Lady Justice statue"></div>
  <p class="front__office">Law Office of Dorian F. Haslbeck</p>
  <div class="front__brand">
    <div class="badge" role="img" aria-label="Membership badge"></div>
    <p class="front__brand-text">PITTSBURGH CRIMINAL DEFENSE ATTORNEY<br>DORIAN F. HASLBECK</p>
  </div>
  <h1 class="front__headline heading"><span class="l1">NEED AN</span><span class="l2">ATTORNEY?</span></h1>
  <p class="front__lead">Attorney Dorian F. Haslbeck has 25 Years of Experience</p>
  <ul class="front__matters">
    <li>All Criminal Matters</li>
    <li>-Most Civil Matters</li>
    <li>-DUI / Traffic Citations / License Restoration</li>
  </ul>
  <p class="front__cta">PLEASE CALL OR EMAIL TODAY FOR YOUR FREE,<br>NO-OBLIGATION INITIAL CONSULTATION.</p>
  <ul class="front__perks" style="color:var(--ink)">
    <li><svg class="check" style="color:var(--red)"><use href="#tick"/></svg>Free Consultation</li>
    <li><svg class="check" style="color:var(--red)"><use href="#tick"/></svg>Affordable Fees</li>
    <li><svg class="check" style="color:var(--red)"><use href="#tick"/></svg>Credit Cards Accepted</li>
  </ul>
  <div class="front__bar">
    <div class="front__phone">
      <svg width="18" height="18" viewBox="0 0 24 24"><path fill="#fff" d="M6.6 10.8a15.2 15.2 0 0 0 6.6 6.6l2.2-2.2a1 1 0 0 1 1-.25 11.4 11.4 0 0 0 3.6.57 1 1 0 0 1 1 1V20a1 1 0 0 1-1 1A17 17 0 0 1 3 4a1 1 0 0 1 1-1h3.5a1 1 0 0 1 1 1c0 1.25.2 2.45.57 3.57a1 1 0 0 1-.25 1z"/></svg>
      412-555-0187
    </div>
    <p class="front__web">www.lakesidedefenselawyer.example <span>|</span> www.dfhcounsel.example</p>
  </div>
</section>

<section class="card card--back">
  <h2 class="back__title heading">PITTSBURGH CRIMINAL DEFENSE ATTORNEY<br>DORIAN F. HASLBECK</h2>
  <p class="back__tag">EXPERIENCE YOU CAN AFFORD</p>
  <ul class="back__questions">
    <li><svg class="check" style="color:#fff"><use href="#tick"/></svg>Charged with DUI?</li>
    <li><svg class="check" style="color:#fff"><use href="#tick"/></svg>Injured in an Auto Accident?</li>
    <li><svg class="check" style="color:#fff"><use href="#tick"/></svg>Recently Arrested?</li>
    <li><svg class="check" style="color:#fff"><use href="#tick"/></svg>Want an Experienced Attorney who Charges</li>
    <li><svg class="check" style="color:#fff"><use href="#tick"/></svg>Reasonable Fees?</li>
  </ul>
  <div class="back__photo" role="img" aria-label="Photo of a police officer writing a citation inside a patrol car"></div>
  <p class="back__cta">PLEASE CALL OR EMAIL TODAY FOR YOUR FREE,<br>NO-OBLIGATION INITIAL CONSULTATION.</p>

  <address class="back__address" style="font-style:normal">
    <span class="name">The Law Office of Dorian F. Haslbeck</span><br>
    1400 Counsel Tower<br>
    275 Harbor Street<br>
    Pittsburgh, PA 15299<br>
    TEL: 412-555-0187 or 412-555-0142<br>
    www.lakesidedefenselawyer.example<br>
    www.dfhcounsel.example
  </address>
  <div class="back__stamp"></div>
  <div class="back__lines"><span></span><span></span><span></span><span></span><span></span><span></span></div>
  <div class="back__seals">
    <div class="badge" role="img" aria-label="Membership badge"></div>
    <div class="seal--gold" role="img" aria-label="Trial lawyer recognition badge"></div>
    <div class="back__rating"><i></i>CTQ</div>
  </div>
</section>

</body>
</html>
```